Business Cards for New Club President

I would like to get Business cards for the new president of our club. Our organization used Quillora Hub last year to create a logo for an event and we love that logo. The new president really likes the logo and would like to use it for her personal logo. But since it was created for a specific event, it needs to be modified. She would like to keep the same basic design but add a strand of pearls winding through the image.

Contact Information for Business Card

Name of President, email, phone, location

Font styles to use
Serif

Colors
ec1f27
fff4ee

Requirements
Must have
• 1. A modified version of the image we previously purchased from Quillora Hub. (see uploaded image); remove the name of the event and date..
2. A strand of pearls (or individual pearls) gracefully wrapping through the image.
3. The phrase "Kestrelvale Alumnae" or "Kestrelvale Alumnae Chapter" on the design
Nice to have
• Use the original design we purchased from Quillora Hub
Should not have
• Should not have any other colors other than red, white or black.

```html
<!DOCTYPE html>
<html lang="en">
<head>
<meta charset="utf-8">
<title>Kestrelvale Alumnae Chapter – President Business Card</title>
<link rel="stylesheet" href="https://fonts.googleapis.com/css2?family=Cinzel:wght@500;700&family=Tinos&display=swap">
<style>
  :root {
    --backdrop: #2a2a2c;
    --brand-red: #c21f2e;
    --card-white: #ffffff;
    --ink-black: #1c1c1c;
    --shadow: rgba(0, 0, 0, 0.45);
  }
  * { box-sizing: border-box; margin: 0; padding: 0; }
  html, body {
    width: 1200px;
    height: 900px;
    overflow: hidden;
    background: var(--backdrop);
  }
  .canvas {
    width: 1200px;
    height: 900px;
    display: flex;
    flex-direction: column;
    align-items: center;
    justify-content: center;
    gap: 40px;
  }
  .card {
    width: 700px;
    height: 400px;
    border-radius: 26px;
    box-shadow: 0 14px 30px var(--shadow);
    position: relative;
    overflow: hidden;
  }

  .wordmark {
    font-family: "Cinzel", serif;
    font-weight: 500;
    text-align: center;
    line-height: 1.15;
    letter-spacing: 0.04em;
    white-space: nowrap;
  }
  .wordmark__dot {
    border-radius: 50%;
    flex: none;
  }

  /* Front: red with centred wordmark */
  .card--front {
    background: var(--brand-red);
    display: flex;
    flex-direction: column;
    align-items: center;
    justify-content: center;
    gap: 24px;
  }
  .card--front .wordmark { color: var(--card-white); font-size: 40px; }
  .card--front .wordmark__dot {
    width: 170px;
    height: 170px;
    background: var(--card-white);
  }

  /* Back: white with contact details */
  .card--back {
    background: var(--card-white);
    padding: 56px 48px;
  }
  .holder__name {
    font-family: "Cinzel", serif;
    font-weight: 700;
    font-size: 30px;
    color: var(--ink-black);
    letter-spacing: 0.04em;
  }
  .holder__title {
    font-family: "Cinzel", serif;
    font-weight: 700;
    font-size: 18px;
    color: var(--brand-red);
    letter-spacing: 0.06em;
    margin-top: 2px;
  }
  .contact {
    position: absolute;
    left: 48px;
    bottom: 40px;
    font-family: "Tinos", serif;
    font-style: normal;
    font-size: 19px;
    color: var(--ink-black);
    line-height: 1.35;
  }
  .contact__row {
    display: flex;
    align-items: center;
    gap: 10px;
  }
  .contact__icon {
    width: 22px;
    height: 22px;
    flex: none;
  }
  .contact__address { margin-top: 10px; }
  .card--back .brand {
    position: absolute;
    right: 24px;
    top: 44px;
    width: 400px;
    display: flex;
    flex-direction: column;
    align-items: center;
    gap: 20px;
  }
  .card--back .wordmark { color: var(--ink-black); font-size: 25px; }
  .card--back .wordmark__dot {
    width: 190px;
    height: 190px;
    background: var(--brand-red);
  }
</style>
</head>
<body>
<main class="canvas">
  <section class="card card--front" aria-label="Card front">
    <span class="wordmark__dot" aria-hidden="true"></span>
    <p class="wordmark">Kestrelvale Alumnae<br>Chapter</p>
  </section>

  <section class="card card--back" aria-label="Card back">
    <h1 class="holder__name">President Name</h1>
    <p class="holder__title">President</p>

    <div class="brand">
      <span class="wordmark__dot" aria-hidden="true"></span>
      <p class="wordmark">Kestrelvale Alumnae<br>Chapter</p>
    </div>

    <address class="contact">
      <div class="contact__row">
        <svg class="contact__icon" viewBox="0 0 24 24" aria-hidden="true">
          <circle cx="12" cy="12" r="12" fill="var(--brand-red)"/>
          <path d="M8.2 6.5l2 2.3-1.1 1.4c.9 1.8 2.2 3.1 4 4l1.4-1.1 2.3 2-.9 1.9c-4.6-.4-8.6-4.4-9-9z" fill="#fff"/>
        </svg>
        <span>800 555 0147</span>
      </div>
      <div class="contact__row">
        <svg class="contact__icon" viewBox="0 0 24 24" aria-hidden="true">
          <circle cx="12" cy="12" r="12" fill="var(--brand-red)"/>
          <rect x="6" y="8" width="12" height="8.5" fill="none" stroke="#fff" stroke-width="1.5"/>
          <path d="M6 8l6 5 6-5" fill="none" stroke="#fff" stroke-width="1.5"/>
        </svg>
        <span>info@Kestrelvalealumnae.com</span>
      </div>
      <p class="contact__address">418 Larkmoor Street<br>Suite 210, Fenwick Falls<br>MI 49210</p>
    </address>
  </section>
</main>
</body>
</html>
```